Business Card Design Project

I am community manager and social media strategist. I need a double sided business card with company logo and name. Looking for something professional, elegant but also a little bit original.

• - The logo and the colours are the company colours and a required to stay.
- The size should be: 84 x 55 mm (or 3.30 x 2.16)
- The file size should be: 1039 x 697 pixels (300 dpi)
- I'd like rounded corners. :)

Use the following contact information for the card:

Léonie Vardin
Stratégie médias sociaux / community management / édition de sites sociaux
mob. : 0687529103
leonie.vardin@postelune.fr
Twitter. : @lvardin
Skype : vardin.leonie

```html
<!DOCTYPE html>
<html lang="fr">
<head>
<meta charset="utf-8">
<title>Carte de visite — Léonie Vardin</title>
<link rel="stylesheet" href="https://fonts.googleapis.com/css2?family=Cabin:ital,wght@0,400;0,600;0,700;1,400&family=Open+Sans:wght@300;400&display=swap">
<style>
  :root {
    --page: #ffffff;
    --blue-light: #2f76b5;
    --blue-deep: #1f4f8c;
    --charcoal: #3c3d3f;
    --brand-blue: #3a92d6;
    --mark-tint: rgba(190, 214, 240, 0.42);
    --ink-light: #ffffff;
    --ink-soft: #e9eef5;
  }
  * { margin: 0; padding: 0; box-sizing: border-box; }
  html, body {
    width: 1200px;
    height: 393px;
    overflow: hidden;
    background: var(--page);
  }
  .sheet {
    position: relative;
    width: 1200px;
    height: 393px;
  }
  .card {
    position: absolute;
    top: 19px;
    width: 542px;
    height: 354px;
    border-radius: 32px;
    overflow: hidden;
    background: linear-gradient(100deg, var(--blue-light), var(--blue-deep));
  }
  .card--front { left: 35px; }
  .card--back { left: 629px; }
  .card__shape {
    position: absolute;
    inset: 0;
    width: 100%;
    height: 100%;
  }
  .brand-mark { fill: var(--mark-tint); }
  .brand-name {
    font-family: "Cabin", sans-serif;
    font-weight: 700;
    fill: var(--brand-blue);
  }
  .identity {
    position: absolute;
    top: 36px;
    right: 60px;
    color: var(--ink-light);
  }
  .identity__name {
    font-family: "Cabin", sans-serif;
    font-weight: 600;
    font-size: 30px;
    letter-spacing: 1px;
    word-spacing: 4px;
    line-height: 1.1;
  }
  .identity__roles {
    list-style: none;
    margin-top: 5px;
    margin-left: 32px;
    margin-right: -30px;
    font-family: "Cabin", sans-serif;
    font-style: italic;
    font-size: 16px;
    line-height: 19px;
    color: var(--ink-soft);
  }
  .contact {
    position: absolute;
    right: 25px;
    top: 226px;
    list-style: none;
    text-align: right;
    font-family: "Open Sans", sans-serif;
    font-weight: 400;
    font-size: 19.5px;
    line-height: 26px;
    color: var(--ink-light);
  }
</style>
</head>
<body>
<main class="sheet">

  <section class="card card--front" aria-label="Recto">
    <svg class="card__shape" viewBox="0 0 542 354" aria-hidden="true">
      <path d="M0,91 C160,115 360,210 542,318 L542,354 L0,354 Z" fill="var(--charcoal)"/>
    </svg>
    <svg class="card__shape" viewBox="0 0 542 354" role="img" aria-label="Emplacement du symbole de la marque">
      <circle class="brand-mark" cx="329" cy="110" r="180"/>
    </svg>
    <svg class="card__shape" viewBox="0 0 542 354" aria-label="VENTARA">
      <text class="brand-name" x="-4" y="343" font-size="132" textLength="520" lengthAdjust="spacingAndGlyphs">VENTARA</text>
    </svg>
  </section>

  <section class="card card--back" aria-label="Verso">
    <svg class="card__shape" viewBox="0 0 542 354" aria-hidden="true">
      <path d="M52,354 C160,255 340,190 542,168 L542,354 Z" fill="var(--charcoal)"/>
    </svg>
    <svg class="card__shape" viewBox="0 0 542 354" role="img" aria-label="Emplacement du symbole de la marque">
      <circle class="brand-mark" cx="109" cy="169" r="137"/>
    </svg>

    <header class="identity">
      <h1 class="identity__name">Léonie Vardin</h1>
      <ul class="identity__roles">
        <li>Stratégie médias sociaux</li>
        <li>Community management</li>
        <li>Édition de sites sociaux</li>
      </ul>
    </header>

    <ul class="contact">
      <li>mob. : 0687529103</li>
      <li>@: leonie.vardin@postelune.fr</li>
      <li>Twitter. : @lvardin</li>
      <li>Skype : vardin.leonie</li>
    </ul>
  </section>

</main>
</body>
</html>
```